Summit Tandem Trial Poster

I need an 11x17 poster using the details attached.

I also attached a poster that I got through Pixelvane and used for our last contest so you know what I liked. I am not looking for the same thing I am just including it so you know my taste. Clean and effective.

Included is the Volcora Bootcamps logo as well.

```html
<!DOCTYPE html>
<html lang="en">
<head>
<meta charset="utf-8">
<title>Summit Tandem Trial Poster</title>
<link href="https://fonts.googleapis.com/css2?family=Graduate&family=Oswald:wght@500;700&family=Staatliches&family=Bowlby+One+SC&display=swap" rel="stylesheet">
<style>
  :root {
    --paper: #ffffff;
    --ink: #000000;
    --gold: #fcc500;
    --gold-shade: #6b5300;
    --white: #ffffff;
    --logo-bg: #e9e9e9;
    --logo-ink: #2b5f9e;
  }
  * { margin: 0; padding: 0; box-sizing: border-box; }
  html, body { width: 1200px; height: 1200px; overflow: hidden; background: var(--paper); }
  .poster {
    position: absolute; left: 308px; top: 148px; width: 584px; height: 904px;
    background: var(--ink); overflow: hidden; text-align: center;
  }
  .corner-glow {
    position: absolute; inset: 0;
    background: linear-gradient(152deg, transparent 80%, var(--gold) 96%);
    pointer-events: none;
  }
  .brand {
    position: absolute; left: 215px; top: 28px; width: 155px; height: 48px;
    background: var(--logo-bg); display: flex; align-items: center; justify-content: center;
    font-family: "Oswald", sans-serif; font-weight: 700; font-size: 17px; line-height: 1;
    color: var(--logo-ink); letter-spacing: .5px;
  }
  .tagline {
    position: absolute; left: 0; right: 0; top: 104px;
    font-family: "Graduate", serif; color: var(--gold);
    font-size: 21.5px; line-height: 26px; transform: rotate(-3deg);
  }
  .art {
    position: absolute; left: 138px; top: 208px; width: 346px; height: 128px;
    background: radial-gradient(ellipse at 50% 60%, var(--gold) 40%, #b38c00 100%);
    border-radius: 40% 40% 10% 10%;
  }
  .title { position: absolute; left: 0; top: 0; width: 584px; height: 520px; color: var(--gold); font-weight: 400; }
  .title-ordinal {
    position: absolute; left: 62px; top: 330px; font-family: "Bowlby One SC", sans-serif;
    font-size: 62px; line-height: 1; letter-spacing: -3px;
    transform: scaleY(1.8); transform-origin: left top;
    text-shadow: 3px 3px 0 var(--gold-shade);
  }
  .title-name {
    position: absolute; left: 192px; top: 340px; font-family: "Staatliches", sans-serif;
    font-size: 52px; line-height: 1; white-space: nowrap; transform: rotate(-3deg);
    text-shadow: 3px 3px 0 var(--gold-shade);
  }
  .title-trial {
    position: absolute; left: 150px; width: 340px; top: 392px; font-family: "Bowlby One SC", sans-serif;
    font-size: 68px; line-height: 1; letter-spacing: 3px; transform: rotate(-3deg);
    text-align: center; text-shadow: 4px 4px 0 var(--gold-shade);
  }
  .section-head {
    position: absolute; left: 0; right: 0; font-family: "Staatliches", sans-serif;
    color: var(--gold); font-size: 37px; line-height: 1; letter-spacing: 2.5px; font-weight: 400;
  }
  .section-body {
    position: absolute; left: 0; right: 0; font-family: "Oswald", sans-serif; font-weight: 500;
    color: var(--white); font-size: 12px; line-height: 15.5px; text-transform: uppercase;
  }
  .program-head { top: 520px; }
  .program-body { top: 556px; }
  .trial-head { top: 611px; }
  .trial-body { top: 647px; }
  .details {
    position: absolute; left: 0; right: 0; top: 724px; font-family: "Staatliches", sans-serif;
    color: var(--gold); font-size: 19px; line-height: 20px; letter-spacing: 2.2px;
  }
  .contact {
    position: absolute; left: 0; right: 0; top: 822px; font-family: "Oswald", sans-serif;
    font-weight: 700; color: var(--white); font-size: 19.5px; line-height: 24px;
  }
</style>
</head>
<body>
  <main class="poster">
    <div class="corner-glow"></div>
    <div class="brand">Volcora Bootcamps</div>
    <p class="tagline">A GOOD REASON<br>TO GET IN<br>THE BEST SHAPE OF YOUR LIFE</p>
    <div class="art" role="img" aria-label="Illustration of two flexing athletes standing back to back"></div>
    <h1 class="title">
      <span class="title-ordinal">1ST</span>
      <span class="title-name">SUMMIT TANDEM</span>
      <span class="title-trial">TRIAL</span>
    </h1>
    <h2 class="section-head program-head">THE PERFECT PROGRAM</h2>
    <p class="section-body program-body">Our 21 day fitness challenge will give you the world class training and testing<br>to ensure that you are prepared to take on anything that life throws at you be in<br>the best shape of your life at the end of 21 days!</p>
    <h2 class="section-head trial-head">SUMMIT TANDEM TRIAL</h2>
    <p class="section-body trial-body">Test you on your initial fitness skills<br>Train you in an intense training program for 21 days<br>Re-test you to see if your team made improvement</p>
    <p class="details">JANUARY 26TH TO FEBRUARY 15TH.<br>OVER $700 IN CASH PRIZES ARE UP FOR GRABS FOR THE<br>BEST TEAM SCORES AND BEST IMPROVEMENT!<br>MALE, FEMALE &amp; CO-ED DIVISIONS!</p>
    <p class="contact">CALL 555-014-2290 TO RESERVE YOUR SPOT TODAY!<br>www.Volcorafit.com</p>
  </main>
</body>
</html>
```